依頼概要
■ 依頼の目的/概要

当社は、「ムテラン」というサイトで似顔絵の売買仲介サービスをご提供しています。リニューアルに伴い、トップページデザイン(コーディング無し)を募集させて頂きます。

考慮していただきたい点は以下の通りです。
・似顔絵サイトなので商品画像が映えるようなデザイン
・基本的な構成は現在のサイトと同じ(横幅950px、2カラム)
・ヘッダーと右カラムはどのページでも共通に表示
・右カラムは、デザインを崩さない程度にできるだけ狭く表示
・「ムテラン」というロゴのデザインもお願いします
・コンテンツは現状のものでも大幅に変えていただいても構いません(可能ならば他ページのコンテンツも見て新たに考えていただければと思います)
・選ばせていただいた方には、他ページにも汎用的に使える見出しタグ(h1,h2,h3)のデザインもお願いします
・作成頂いたウェブサイトをベースに他ページも制作したい(追加料金を払ってお願いする可能性もあります)

・現在のウェブサイト
http://mutelan-site.jp/

■ 納品ファイルの希望

Illustrator、Photoshop、 InkScape、Gimp形式のいづれか

■ その他/注意点

選択させて頂いたウェブデザインの著作権(財産権)等の扱いはWorvex利用規約に従い、弊社に譲渡をお願いします。フォントや画像素材などを利用する場合は上記利用用途に使用できることを確認し、第三者の知的財産権等に注意して下さい。
■ 選んだ理由

コンセプトが一番はっきりしており、デザインもまとまりがあるように感じました。
現在のデザインから、ガラッとイメージが変わったのも良かったです。

パーツで見ると他の方の作品も素晴らしいのですが、まとまりを重視させていただきました。

■ 提案者全員のお礼・コメント

予想以上に多くの方、素晴らしいデザインをご提供していただきまして、ありがとうございました。

```html
<!DOCTYPE html>
<html lang="ja">
<head>
<meta charset="utf-8">
<title>ムテラン | 似顔絵師のための売買仲介サイト</title>
<link href="https://fonts.googleapis.com/css2?family=Noto+Sans+JP:wght@400;700&display=swap" rel="stylesheet">
<style>
:root{
  --blue:#2b8fd6;
  --blue-dark:#1f6fb0;
  --blue-pale:#e6f2fb;
  --orange:#f39a1e;
  --orange-pale:#fff3df;
  --page:#eef2f5;
  --line:#d5dde4;
  --text:#333;
  --muted:#777;
  --link:#2a73c2;
  --white:#fff;
}
*{box-sizing:border-box;margin:0;padding:0}
html,body{width:833px;height:1200px;overflow:hidden}
body{font-family:"Noto Sans JP",sans-serif;color:var(--text);background:var(--page);font-size:10px;position:relative}
a{color:var(--link);text-decoration:none}
.site{position:absolute;left:0;top:0;width:833px;height:1200px;background:var(--white)}
.header{position:absolute;left:33px;top:10px;width:772px;height:80px}
.brand{position:absolute;left:0;top:10px;display:flex;align-items:center;gap:10px}
.brand-mark{width:18px;height:18px;border-radius:50%;background:var(--blue)}
.brand-name{font-size:30px;font-weight:700;color:var(--blue);letter-spacing:1px}
.brand-tagline{font-size:11px;color:var(--blue-dark);margin-left:6px}
.util-links{position:absolute;right:0;top:14px;display:flex;gap:16px;font-size:10px}
.util-links a{color:var(--muted);display:flex;align-items:center;gap:4px}
.util-links svg{width:12px;height:12px}
.gnav{position:absolute;left:33px;top:100px;width:772px;height:40px;background:linear-gradient(#fafcfd,#e3ebf1);border:1px solid var(--line);display:flex}
.gnav a{flex:1;display:flex;align-items:center;justify-content:center;font-size:12px;color:var(--text);border-right:1px solid var(--line)}
.gnav a:last-child{border-right:0}
.gnav a.is-active{background:var(--blue);color:var(--white);font-weight:700}
.main{position:absolute;left:33px;top:153px;width:540px}
.side{position:absolute;left:585px;top:161px;width:220px}
.hero{width:540px;height:214px;border-radius:4px;background:linear-gradient(135deg,#d9eefb,#bfe0f5 55%,#fbe3b5)}
.sec-head{display:flex;justify-content:space-between;align-items:center;border-bottom:2px solid var(--blue);padding:0 0 4px 8px;position:relative}
.sec-head::before{content:"";position:absolute;left:0;top:2px;width:4px;height:14px;background:var(--blue)}
.sec-head h2{font-size:12px;font-weight:700}
.more{font-size:9px;color:var(--muted);border:1px solid var(--line);padding:1px 10px;border-radius:2px;background:#f7f9fb}
.creators{margin-top:22px}
.creator-list{display:flex;gap:9px;margin-top:10px}
.creator{width:100px;text-align:center;font-size:9px}
.creator .thumb{height:111px;border-radius:3px;background:linear-gradient(160deg,#fde4c8,#f6b9a0)}
.creator:nth-child(2) .thumb{background:linear-gradient(160deg,#e8e0f6,#b9a7e2)}
.creator:nth-child(3) .thumb{background:linear-gradient(160deg,#fdf1c4,#f3c86a)}
.creator:nth-child(4) .thumb{background:linear-gradient(160deg,#d7efe0,#94cfa9)}
.creator:nth-child(5) .thumb{background:linear-gradient(160deg,#d9ebfa,#8fbfe6)}
.creator a{display:block;margin-top:8px}
.products{margin-top:22px}
.product-list{display:flex;gap:14px;margin-top:12px}
.product{flex:1;display:flex;gap:10px;border:1px solid var(--line);padding:8px;border-radius:3px;height:150px;min-width:0}
.product .thumb{width:104px;flex:none;background:linear-gradient(160deg,#f4e6d6,#d9b794);border-radius:2px}
.product:nth-child(2) .thumb{background:linear-gradient(160deg,#dbe9f4,#9ab8d2)}
.product-body{min-width:0}
.product h3{font-size:9.5px;color:var(--link);font-weight:700;margin-bottom:5px;white-space:nowrap}
.product dl{font-size:9px;line-height:1.75}
.product dt{display:inline;color:var(--muted)}
.product dd{display:inline}
.product dd::after{content:"";display:block}
.news{margin-top:22px}
.news-list{list-style:none;margin-top:10px}
.news-list li{display:flex;gap:16px;font-size:10px;padding:6px 6px;border-bottom:1px dotted var(--line)}
.news-list time{color:var(--muted)}
.signup{display:block;border-radius:4px;padding:10px;height:94px;margin-bottom:23px}
.signup.user{background:var(--blue-pale);border:2px solid var(--blue)}
.signup.creator-join{background:var(--orange-pale);border:2px solid var(--orange)}
.signup p{font-size:11px;font-weight:700;margin-bottom:8px}
.signup.user p{color:var(--blue-dark)}
.signup.creator-join p{color:#c97300}
.signup .btn{display:flex;align-items:center;justify-content:center;height:40px;border-radius:3px;color:var(--white);font-size:13px;font-weight:700}
.signup.user .btn{background:var(--blue)}
.signup.creator-join .btn{background:var(--orange)}
.panel{border:1px solid var(--line);border-radius:3px;margin-bottom:14px}
.panel h2{font-size:12px;font-weight:700;padding:7px 10px;background:linear-gradient(#fbfcfd,#e9eff4);border-bottom:1px solid var(--line);display:flex;align-items:center;gap:6px}
.panel h2::before{content:"";width:10px;height:10px;border-radius:50%;background:var(--blue)}
.ranking{list-style:none;padding:8px 10px}
.ranking li{display:flex;align-items:center;gap:8px;padding:4px 0;font-size:9px}
.ranking .rank{width:14px;height:14px;border-radius:50%;background:var(--orange);color:var(--white);font-size:8px;display:flex;align-items:center;justify-content:center;font-weight:700}
.ranking .thumb{width:26px;height:26px;border-radius:2px;background:linear-gradient(160deg,#fde4c8,#f0a98c)}
.search{padding:8px 10px}
.field{display:flex;align-items:center;justify-content:space-between;font-size:9px;margin-bottom:7px}
.select{width:120px;height:18px;border:1px solid var(--line);border-radius:2px;display:flex;align-items:center;justify-content:space-between;padding:0 5px;color:var(--muted);font-size:9px}
.select::after{content:"▼";font-size:7px}
.radios{width:120px;display:flex;gap:10px;font-size:9px}
.radios span::before{content:"";display:inline-block;width:8px;height:8px;border:1px solid var(--muted);border-radius:50%;margin-right:3px;vertical-align:-1px}
.search-btn{display:block;margin:10px auto 4px;width:110px;height:26px;border-radius:3px;background:linear-gradient(#fdfefe,#dde6ee);border:1px solid var(--line);font-size:11px;font-weight:700;text-align:center;line-height:24px;color:var(--text)}
.cat{padding:8px 12px;font-size:9px}
.cat h3{font-size:9px;color:var(--muted);margin:2px 0 4px}
.cat ul{list-style:none;display:grid;grid-template-columns:1fr 1fr;gap:4px 8px;margin-bottom:6px}
.cat li::before{content:"▸ ";color:var(--blue)}
.pagetop{position:absolute;right:28px;top:1052px;background:var(--blue);color:var(--white);font-size:9px;padding:5px 12px;border-radius:3px}
.footer{position:absolute;left:0;top:1086px;width:833px;height:114px;background:var(--page);border-top:3px solid var(--blue)}
.footer-links{position:absolute;left:33px;top:22px;display:flex;gap:16px;font-size:9px}
.footer-links a{color:var(--link)}
.copyright{position:absolute;right:28px;top:22px;font-size:9px;color:var(--muted)}
</style>
</head>
<body>
<div class="site">
  <header class="header">
    <div class="brand">
      <span class="brand-mark"></span>
      <span class="brand-name">ムテラン</span>
      <span class="brand-tagline">似顔絵師のための売買仲介サイト</span>
    </div>
    <nav class="util-links">
      <a href="#"><svg viewBox="0 0 12 12"><rect x="1" y="2" width="10" height="8" rx="1" fill="none" stroke="#2b8fd6"/><path d="M1 3l5 4 5-4" fill="none" stroke="#2b8fd6"/></svg>お問い合わせ</a>
      <a href="#"><svg viewBox="0 0 12 12"><circle cx="6" cy="4" r="2.5" fill="#2b8fd6"/><path d="M1.5 11c0-3 9-3 9 0z" fill="#2b8fd6"/></svg>マイページ</a>
      <a href="#"><svg viewBox="0 0 12 12"><path d="M2 6h6M6 3l3 3-3 3" fill="none" stroke="#2b8fd6" stroke-width="1.5"/></svg>ログイン</a>
    </nav>
  </header>

  <nav class="gnav">
    <a href="#" class="is-active">トップ</a>
    <a href="#">クリエイター一覧</a>
    <a href="#">商品一覧</a>
    <a href="#">ムテランとは</a>
    <a href="#">会員登録</a>
    <a href="#">お問い合わせ</a>
  </nav>

  <main class="main">
    <div class="hero" role="img" aria-label="似顔絵作品の並ぶメインビジュアル。「使い方自由!あなた次第!」「絵柄を選べる!!」の手描き文字と筆のイラスト"></div>

    <section class="creators">
      <div class="sec-head"><h2>新着似顔絵クリエイター</h2><a class="more" href="#">一覧</a></div>
      <div class="creator-list">
        <div class="creator"><div class="thumb" role="img" aria-label="クリエイターの似顔絵作品"></div><a href="#">ミナト</a></div>
        <div class="creator"><div class="thumb" role="img" aria-label="クリエイターの似顔絵作品"></div><a href="#">KAEDE</a></div>
        <div class="creator"><div class="thumb" role="img" aria-label="クリエイターの似顔絵作品"></div><a href="#">ハルノ</a></div>
        <div class="creator"><div class="thumb" role="img" aria-label="クリエイターの似顔絵作品"></div><a href="#">sora</a></div>
        <div class="creator"><div class="thumb" role="img" aria-label="クリエイターの似顔絵作品"></div><a href="#">MOMO</a></div>
      </div>
    </section>

    <section class="products">
      <div class="sec-head"><h2>商品新作情報</h2><a class="more" href="#">一覧</a></div>
      <div class="product-list">
        <article class="product">
          <div class="thumb" role="img" aria-label="家族の似顔絵作品"></div>
          <div class="product-body">
            <h3>★似顔絵(ファミリーセット)</h3>
            <dl>
              <dt>【価格】</dt><dd>似顔絵1人 3,000円</dd>
              <dt>【納期】</dt><dd>約7日〜10日</dd>
              <dt>【サイズ】</dt><dd>A4サイズ</dd>
              <dt>【作風】</dt><dd>水彩風</dd>
              <dt>【カラー】</dt><dd>フルカラー</dd>
            </dl>
          </div>
        </article>
        <article class="product">
          <div class="thumb" role="img" aria-label="ビジネス向け似顔絵作品"></div>
          <div class="product-body">
            <h3>プロフィール用似顔絵</h3>
            <dl>
              <dt>【価格】</dt><dd>似顔絵1人 2,500円</dd>
              <dt>【納期】</dt><dd>約5日〜7日</dd>
              <dt>【サイズ】</dt><dd>データ納品</dd>
              <dt>【作風】</dt><dd>デジタル</dd>
              <dt>【カラー】</dt><dd>フルカラー</dd>
            </dl>
          </div>
        </article>
      </div>
    </section>

    <section class="news">
      <div class="sec-head"><h2>お知らせ</h2></div>
      <ul class="news-list">
        <li><time>2011.02.15</time><a href="#">似顔絵サイト「ムテラン」がオープンしました。</a></li>
        <li><time>2011.02.14</time><a href="#">似顔絵サイト「ムテラン」がオープンしました。</a></li>
        <li><time>2011.02.13</time><a href="#">似顔絵サイト「ムテラン」がオープンしました。</a></li>
        <li><time>2011.02.12</time><a href="#">似顔絵サイト「ムテラン」がオープンしました。</a></li>
        <li><time>2011.02.10</time><a href="#">似顔絵サイト「ムテラン」がオープンしました。</a></li>
      </ul>
    </section>
  </main>

  <aside class="side">
    <a class="signup user" href="#"><p>個人さんはこちら</p><span class="btn">ユーザー会員登録</span></a>
    <a class="signup creator-join" href="#"><p>販売したい方</p><span class="btn">クリエイター会員登録</span></a>

    <section class="panel">
      <h2>クリエイターランキング</h2>
      <ol class="ranking">
        <li><span class="rank">1</span><span class="thumb" role="img" aria-label="似顔絵作品"></span><a href="#">KAEDE (似顔絵師)</a></li>
        <li><span class="rank">2</span><span class="thumb" role="img" aria-label="似顔絵作品"></span><a href="#">ミナト</a></li>
        <li><span class="rank">3</span><span class="thumb" role="img" aria-label="似顔絵作品"></span><a href="#">ユズリハ</a></li>
      </ol>
    </section>

    <section class="panel">
      <h2>クリエイター検索</h2>
      <div class="search">
        <div class="field"><span>カテゴリ</span><span class="select">指定なし</span></div>
        <div class="field"><span>性別</span><span class="radios"><span>女性</span><span>男性</span></span></div>
        <div class="field"><span>価格帯</span><span class="select">下限なし</span></div>
        <div class="field"><span></span><span class="select">上限なし</span></div>
        <div class="field"><span>納期</span><span class="select">指定なし</span></div>
        <div class="field"><span>画風</span><span class="select">指定なし</span></div>
        <div class="field"><span>ユーザー評価</span><span class="select">指定なし</span></div>
        <a class="search-btn" href="#">検索する</a>
      </div>
    </section>

    <section class="panel">
      <h2>カテゴリから検索</h2>
      <div class="cat">
        <h3>クリエイター</h3>
        <ul><li><a href="#">似顔絵</a></li><li><a href="#">似顔絵</a></li><li><a href="#">イラスト</a></li><li><a href="#">名刺用</a></li></ul>
        <h3>商品</h3>
        <ul><li><a href="#">似顔絵</a></li><li><a href="#">似顔絵</a></li></ul>
      </div>
    </section>
  </aside>

  <a class="pagetop" href="#">▲ ページトップへ</a>

  <footer class="footer">
    <nav class="footer-links">
      <a href="#">特定商取引に関する表記</a>
      <a href="#">利用規約</a>
      <a href="#">個人情報保護</a>
      <a href="#">お問い合わせ</a>
    </nav>
    <p class="copyright">Copyright © Mutelan. All Rights Reserved.</p>
  </footer>
</div>
</body>
</html>
```